Promotional Ad/Flyer - KVP Leasing

A division of our company, KVP Leasing (kvp-leasing.example) is celebrating its 1-year anniversary in September and we would like to run a promotion. I am looking to have a promotional ad/flyer made-up for email mailings and LinkedIn posts and possibly have on our site. Have plenty of product photos to share if needed, not a prerequisite to use our product in the ad but open to it. Can also be cool graphics as well. We want to capture the viewers attention with the 30 DAYS FREE! The message is simple:
We are celebrating our 1-Year Anniversary by offering a Special Peak-Season Promotion!

FREE RENTALS for 30 days with a minimum 30-Day rental!

Valid from Sep. 1 - Dec. 31 & while supplies last.

Please contact our sales department for more details.

Email: rfq@kvp-leasing.example
Phone: +1-555-284-3917

```html
<!DOCTYPE html>
<html lang="en">
<head>
<meta charset="utf-8">
<title>KVP Leasing – 1st Year Anniversary Promotion</title>
<link href="https://fonts.googleapis.com/css2?family=Anton&family=Montserrat:wght@300;400;500;600;800&family=Roboto+Condensed:wght@700&family=Roboto:wght@400&display=swap" rel="stylesheet">
<style>
  :root {
    --brand-blue: #4a6fb5;
    --slate: #3e4b5e;
    --ink: #0d0d0d;
    --muted: #5a5f66;
    --paper-light: #f6f5f5;
    --paper-dark: #dcdada;
    --white: #ffffff;
  }
  * { margin: 0; padding: 0; box-sizing: border-box; }
  html, body { width: 873px; height: 1200px; overflow: hidden; background: var(--paper-light); }
  .flyer {
    position: relative;
    width: 873px;
    height: 1200px;
    overflow: hidden;
    font-family: "Montserrat", sans-serif;
  }
  .flyer__backdrop {
    position: absolute; inset: 0;
    background:
      linear-gradient(155deg, rgba(255,255,255,0.85) 0%, rgba(255,255,255,0) 40%),
      linear-gradient(180deg, var(--paper-light) 0%, #ebe9e9 55%, var(--paper-dark) 100%);
  }
  .brand-mark {
    position: absolute; left: 77px; top: 100px;
    width: 120px; height: 120px;
    background: var(--brand-blue);
  }
  .brand-name {
    position: absolute; left: 230px; top: 118px; width: 566px;
    text-align: right;
    font-weight: 800; font-size: 64px; line-height: 1;
    color: var(--ink); letter-spacing: 1px;
  }
  .brand-tagline {
    position: absolute; right: 77px; top: 230px;
    font-size: 14px; font-weight: 500; letter-spacing: 2px;
    color: var(--muted);
  }
  .headline-intro {
    position: absolute; left: 116px; top: 336px; width: 641px;
    text-align: center; font-size: 41px; font-weight: 600;
    color: var(--slate); letter-spacing: -0.5px; white-space: nowrap;
  }
  .anniversary { color: var(--brand-blue); }
  .anniversary__one {
    position: absolute; left: 118px; top: 392px;
    font-size: 208px; font-weight: 600; line-height: 1; letter-spacing: -6px;
  }
  .anniversary__suffix {
    position: absolute; left: 218px; top: 398px;
    font-size: 112px; font-weight: 500; line-height: 1; letter-spacing: -3px;
  }
  .anniversary__year {
    position: absolute; left: 344px; top: 456px;
    font-size: 50px; font-weight: 500; line-height: 1;
  }
  .anniversary__word {
    position: absolute; left: 224px; top: 516px;
    font-size: 68px; font-weight: 500; line-height: 1; letter-spacing: 0.5px;
  }
  .promo-lead {
    position: absolute; left: 116px; top: 602px; width: 641px;
    text-align: center; font-size: 21px; font-weight: 300;
    color: var(--slate); white-space: nowrap; letter-spacing: -0.3px;
  }
  .offer-box {
    position: absolute; left: 116px; top: 653px;
    width: 641px; height: 133px;
    border: 2px solid var(--brand-blue);
    display: flex; align-items: center; justify-content: center;
  }
  .offer-box__text {
    font-family: "Anton", sans-serif;
    font-size: 106px; line-height: 1; color: var(--brand-blue);
    letter-spacing: 1px; transform: scaleY(1.16);
  }
  .offer-duration {
    position: absolute; left: 110px; top: 798px; width: 653px;
    text-align: center; font-size: 92px; font-weight: 500; line-height: 1;
    color: var(--slate); white-space: nowrap; letter-spacing: -1px;
  }
  .offer-condition {
    position: absolute; left: 116px; top: 886px; width: 641px;
    text-align: center; font-size: 34px; font-weight: 600;
    color: var(--slate); white-space: nowrap; letter-spacing: -0.5px;
  }
  .validity-pill {
    position: absolute; left: 117px; top: 944px;
    width: 639px; height: 60px; border-radius: 30px;
    background: var(--brand-blue); color: var(--white);
    display: flex; align-items: center; justify-content: center;
    font-size: 21px; font-weight: 300; white-space: nowrap;
  }
  .contact-call {
    position: absolute; left: 116px; top: 1026px; width: 641px;
    text-align: center;
    font-family: "Roboto Condensed", sans-serif; font-weight: 700;
    font-size: 20px; color: var(--ink);
  }
  .contact-list {
    position: absolute; left: 0; top: 1074px; width: 873px;
    display: flex; justify-content: center; gap: 22px;
    list-style: none;
  }
  .contact-item {
    display: flex; align-items: center; gap: 6px;
    font-family: "Roboto", sans-serif; font-size: 19px; color: var(--ink);
  }
  .contact-item__icon { width: 30px; height: 30px; flex: none; }
</style>
</head>
<body>
<main class="flyer">
  <div class="flyer__backdrop" role="img" aria-label="Soft, faded photo of a riveted aluminium air cargo container"></div>

  <div class="brand-mark" aria-hidden="true"></div>
  <div class="brand-name">KVP LEASING</div>
  <div class="brand-tagline">KVP-LEASING.EXAMPLE &nbsp;|&nbsp; BY NORVIK</div>

  <h1 class="headline-intro">WE ARE CELEBRATING OUR</h1>
  <div class="anniversary">
    <span class="anniversary__one">1</span>
    <span class="anniversary__suffix">st</span>
    <span class="anniversary__year">YEAR</span>
    <span class="anniversary__word">ANNIVERSARY</span>
  </div>
  <p class="promo-lead">BY OFFERING A SPECIAL PEAK-SEASON PROMOTION!</p>

  <div class="offer-box"><span class="offer-box__text">FREE RENTALS</span></div>
  <p class="offer-duration">FOR 30 DAYS</p>
  <p class="offer-condition">WITH A MINIMUM 30-DAY RENTAL!</p>

  <div class="validity-pill">VALID FROM SEP. 1 - DEC. 31 &amp; WHILE SUPPLIES LAST.</div>

  <p class="contact-call">PLEASE CONTACT OUR SALES DEPARTMENT FOR MORE DETAILS</p>
  <ul class="contact-list">
    <li class="contact-item">
      <svg class="contact-item__icon" viewBox="0 0 30 30" aria-hidden="true">
        <circle cx="15" cy="15" r="15" fill="#4a6fb5"/>
        <rect x="7.5" y="10" width="15" height="10.5" rx="1" fill="none" stroke="#fff" stroke-width="1.4"/>
        <path d="M7.8 10.5 L15 16 L22.2 10.5 M7.8 20 L12.8 15 M22.2 20 L17.2 15" fill="none" stroke="#fff" stroke-width="1.3"/>
      </svg>
      rfq@kvp-leasing.example
    </li>
    <li class="contact-item">
      <svg class="contact-item__icon" viewBox="0 0 30 30" aria-hidden="true">
        <circle cx="15" cy="15" r="15" fill="#4a6fb5"/>
        <path d="M10.5 7.5 c1 0 1.6 .5 2 1.4 l1 2.3 c.3 .8 .1 1.5-.5 2 l-1 .9 c.8 1.8 2.2 3.3 4 4.2 l.9-1 c.6-.6 1.3-.7 2-.4 l2.3 1 c.9 .4 1.3 1 1.3 2 v1.4 c0 1.2-1 2.1-2.2 2 C13.6 22.6 7.4 16.4 7 9.7 6.9 8.5 7.8 7.5 9 7.5 z" fill="#fff"/>
      </svg>
      +1-555-284-3917
    </li>
  </ul>
</main>
</body>
</html>
```